3.5inch x 8.5inch door hangar

this project is for a 3.5x8.5 inch door hangar
i have included the narrative info and logo files

please focus on a graphic that shows a solar patio. i have attached an example, but please create or use your own graphic

```html
<!DOCTYPE html>
<html lang="en">
<head>
<meta charset="utf-8">
<title>Quorvane Solar Door Hanger</title>
<link href="https://fonts.googleapis.com/css2?family=Roboto:wght@500;700;900&family=Roboto+Condensed:wght@400;700&display=swap" rel="stylesheet">
<style>
  :root{
    --navy:#1f3a6e;
    --orange:#e87b26;
    --sky-top:#3f8ad6;
    --sky-mid:#a9cdf0;
    --white:#ffffff;
    --stage:#e6e6e6;
  }
  *{margin:0;padding:0;box-sizing:border-box}
  html,body{width:1200px;height:1200px;overflow:hidden;background:var(--stage)}
  .hanger{
    position:absolute;left:369px;top:40px;width:484px;height:1176px;
    transform:scale(0.952);transform-origin:top left;
    background:var(--white);overflow:hidden;
    box-shadow:0 6px 18px rgba(0,0,0,.25);
    font-family:"Roboto Condensed",Arial,sans-serif;color:var(--navy);
  }
  .sky{position:absolute;left:0;top:0;width:100%;height:232px;
    background:radial-gradient(ellipse at 50% 100%,#ffffff 0%,#e3f0fb 30%,var(--sky-mid) 60%,var(--sky-top) 100%);}
  .brand{position:absolute;top:160px;left:0;width:100%;display:flex;justify-content:center;align-items:center;gap:12px}
  .brand-name{font-family:"Roboto",Arial,sans-serif;font-weight:900;font-size:60px;letter-spacing:1px;color:var(--navy);line-height:1}
  .brand-dot{width:36px;height:36px;border-radius:50%;background:var(--orange)}
  .panel-photo{position:absolute;left:4px;top:265px;width:452px;height:185px;
    background:linear-gradient(160deg,#ffffff 0%,#6c7fc0 35%,#2b3f8f 60%,#c8ccd6 100%);}
  .headline{position:absolute;left:33px;top:470px;font-family:"Roboto",Arial,sans-serif;font-weight:700;font-size:33px;line-height:42px;color:var(--orange)}
  .ticks{position:absolute;list-style:none}
  .ticks li{position:relative;padding-left:32px}
  .ticks li svg{position:absolute;left:0;top:4px;width:24px;height:22px}
  .benefits{left:31px;top:565px;font-size:24px;line-height:30.5px}
  .subhead{position:absolute;left:36px;top:727px;font-weight:700;font-size:36px;color:var(--navy)}
  .structures{left:31px;top:777px;font-size:23px;line-height:28px}
  .structures li{padding-left:34px}
  .footer-band{position:absolute;left:0;top:955px;width:484px;height:221px}
  .toll{position:absolute;top:945px;left:0;width:100%;text-align:center;font-family:"Roboto",Arial,sans-serif;font-weight:500;font-size:32px;color:var(--orange)}
  .phone{position:absolute;left:42px;top:995px;width:385px;height:70px;border:3px solid var(--white);border-radius:22px;background:var(--navy);
    color:var(--white);font-family:"Roboto",Arial,sans-serif;font-weight:700;font-size:44px;letter-spacing:3px;display:flex;align-items:center;justify-content:center;white-space:nowrap}
  .web{position:absolute;top:1082px;left:0;width:100%;text-align:center;font-family:"Roboto",Arial,sans-serif;font-weight:700;font-size:30px;color:var(--white);white-space:nowrap}
</style>
</head>
<body>
<div class="hanger">
  <div class="sky"></div>
  <div class="brand"><span class="brand-name">QUORVANE</span><span class="brand-dot"></span></div>
  <div class="panel-photo" role="img" aria-label="Photo of a tilted row of blue solar panels on a mounting frame"></div>

  <h1 class="headline">Custom Engineered Solar<br>Pations and Structures</h1>

  <ul class="ticks benefits">
    <li><svg viewBox="0 0 24 22"><path d="M2 12 L9 19 L22 3" fill="none" stroke="#e87b26" stroke-width="4"/></svg>Improve your family’s lifestyle</li>
    <li><svg viewBox="0 0 24 22"><path d="M2 12 L9 19 L22 3" fill="none" stroke="#e87b26" stroke-width="4"/></svg>Upgrade your usable space</li>
    <li><svg viewBox="0 0 24 22"><path d="M2 12 L9 19 L22 3" fill="none" stroke="#e87b26" stroke-width="4"/></svg>Lower your current power bills up to 1/2</li>
    <li><svg viewBox="0 0 24 22"><path d="M2 12 L9 19 L22 3" fill="none" stroke="#e87b26" stroke-width="4"/></svg>Increase your home appraisal value<br>using tax creadits</li>
  </ul>

  <h2 class="subhead">Structures to choose from</h2>

  <ul class="ticks structures">
    <li><svg viewBox="0 0 24 22"><path d="M2 12 L9 19 L22 3" fill="none" stroke="#e87b26" stroke-width="4"/></svg>Solar Patios</li>
    <li><svg viewBox="0 0 24 22"><path d="M2 12 L9 19 L22 3" fill="none" stroke="#e87b26" stroke-width="4"/></svg>Solar Carports</li>
    <li><svg viewBox="0 0 24 22"><path d="M2 12 L9 19 L22 3" fill="none" stroke="#e87b26" stroke-width="4"/></svg>Solar RV Parking</li>
    <li><svg viewBox="0 0 24 22"><path d="M2 12 L9 19 L22 3" fill="none" stroke="#e87b26" stroke-width="4"/></svg>Outdoor pool and barbecue decks</li>
    <li><svg viewBox="0 0 24 22"><path d="M2 12 L9 19 L22 3" fill="none" stroke="#e87b26" stroke-width="4"/></svg>Commercial outdoor dining spaces</li>
  </ul>

  <svg class="footer-band" viewBox="0 0 484 221" preserveAspectRatio="none">
    <path d="M0 0 Q242 80 484 0 L484 221 L0 221 Z" fill="#e87b26"/>
  </svg>
  <div class="toll">TOLL FREE CALL</div>
  <div class="phone">555 014 8862</div>
  <div class="web">www.quorvane-solar.example</div>
</div>
</body>
</html>
```